Need a stunning looking Business Card Design for my Telecom Business, Wow FACTOR!

I deal with high level IT Directors , and Contractors.
I need to impress them with a sleek , professional and unique business card.
Im thinking options as far as rounded edges, plastic , or even metal card or die cut on a corner.
Whatever looks better and leave an unforgettable first impression.
im looking for the wow factor.
Front should have the basics info (attached on the picture of current business card)
i would like to add picture of myself somewhere
Back side
should have logo and maybe some pictures or past projects, you can download from my website ( www.lumvexholdings.com)

```html
<!DOCTYPE html>
<html lang="en">
<head>
<meta charset="utf-8">
<title>Lumvex Holdings – Business Card</title>
<link rel="stylesheet" href="https://fonts.googleapis.com/css2?family=Montserrat:wght@400;500;600;700;800&display=swap">
<style>
  :root{
    --stage:#020c17;
    --navy:#0b2550;
    --navy-deep:#07193a;
    --glass:rgba(4,20,38,0.78);
    --glass-edge:rgba(255,255,255,0.28);
    --cyan:#12b5e8;
    --white:#ffffff;
    --green:#6aab08;
    --yellow:#f7d300;
    --orange:#fb8a05;
    --red:#e52a0c;
    --ink:#0a1020;
  }
  *{margin:0;padding:0;box-sizing:border-box}
  html,body{width:1200px;height:1200px;overflow:hidden;background:var(--stage)}
  body{position:relative;font-family:'Montserrat',sans-serif;color:var(--white)}

  .orb{position:absolute;border-radius:50%}
  .orb--green{left:150px;top:174px;width:194px;height:194px;background:linear-gradient(90deg,#5f9a07,#7bb509)}
  .orb--orange{left:840px;top:600px;width:280px;height:280px;background:linear-gradient(110deg,#f7d300 10%,var(--orange) 95%)}
  .orb--red{left:609px;top:857px;width:136px;height:136px;background:var(--red)}

  /* front */
  .card-front{position:absolute;left:246px;top:132px;width:708px;height:406px}
  .front-face{position:absolute;left:200px;top:0;width:508px;height:406px;border-radius:0 56px 56px 0;
    background:linear-gradient(160deg,#0d2c5e 0%,var(--navy) 45%,var(--navy-deep) 100%);overflow:hidden}
  .front-face__pattern{position:absolute;inset:0;
    background:linear-gradient(125deg,rgba(255,255,255,0.05) 0%,rgba(255,255,255,0) 40%,rgba(255,255,255,0.04) 70%,rgba(255,255,255,0) 100%)}
  .glass{position:absolute;border-radius:56px;background:var(--glass);border:1px solid var(--glass-edge);
    backdrop-filter:blur(22px);-webkit-backdrop-filter:blur(22px)}
  .card-front .glass{left:0;top:0;width:278px;height:406px}

  .name-band{position:absolute;left:456px;top:93px;width:252px;height:71px;background:var(--cyan)}
  .portrait-ring{position:absolute;left:324px;top:59px;width:140px;height:140px;border-radius:50%;background:var(--cyan)}
  .portrait{position:absolute;left:18px;top:18px;width:104px;height:104px;border-radius:50%;
    background:radial-gradient(circle at 50% 40%,#c9a98a 0%,#8a7a6e 45%,#5b6470 100%)}
  .person{position:absolute;left:491px;top:108px}
  .person__name{font-size:22px;font-weight:400;color:var(--ink);letter-spacing:0.2px;line-height:1}
  .person__name strong{font-weight:800}
  .person__role{margin-top:7px;font-size:13px;font-weight:500;color:var(--white)}

  .contacts{position:absolute;left:323px;top:242px;list-style:none}
  .contacts li{position:relative;height:26.3px;padding-left:28px;font-size:14px;line-height:20px}
  .contacts svg{position:absolute;left:0;top:2px;width:16px;height:16px}

  /* back */
  .card-back{position:absolute;left:246px;top:666px;width:708px;height:405px}
  .project-photo{position:absolute;left:0;top:0;width:470px;height:405px;border-radius:56px 0 0 56px;
    background:linear-gradient(180deg,#1b3d73 0%,#143264 50%,#0e2550 100%)}
  .card-back .glass{left:430px;top:0;width:278px;height:405px;background:rgba(4,20,38,0.72)}
  .headline{position:absolute;left:43px;top:155px;line-height:1}
  .headline__top{display:block;font-size:32px;font-weight:600}
  .headline__main{display:block;margin-top:10px;font-size:50px;font-weight:800;color:var(--cyan);letter-spacing:0.5px}
  .regions{position:absolute;left:44px;top:350px;display:flex;gap:33px}
  .region{width:90px;height:17px;font-size:11px;line-height:17px;text-align:center;font-weight:500;letter-spacing:0.3px}
  .region--miami{background:linear-gradient(90deg,#f2360c,#d8150c)}
  .region--broward{width:91px;background:linear-gradient(90deg,#f8cf00,#fb9a05);margin-left:0}
  .region--palm{width:91px;background:var(--green)}

  .brand{position:absolute;left:450px;top:220px;width:238px;text-align:center}
  .brand__dot{display:block;width:34px;height:34px;border-radius:50%;background:var(--cyan);margin:0 auto 14px}
  .brand__name{font-size:20px;font-weight:700;letter-spacing:1.5px;color:var(--white);line-height:1.2}
</style>
</head>
<body>

  <div class="orb orb--green"></div>

  <section class="card-front" aria-label="Business card front">
    <div class="front-face"><div class="front-face__pattern"></div></div>
    <div class="glass"></div>

    <div class="name-band"></div>
    <div class="portrait-ring">
      <div class="portrait" role="img" aria-label="Portrait photo of Dario Velmont"></div>
    </div>
    <div class="person">
      <p class="person__name"><strong>Dario</strong> Velmont</p>
      <p class="person__role">Operations Manager</p>
    </div>

    <ul class="contacts">
      <li>
        <svg viewBox="0 0 24 24" fill="none" stroke="#e52a0c" stroke-width="2" stroke-linecap="round" stroke-linejoin="round"><path d="M22 16.9v3a2 2 0 0 1-2.2 2 19.8 19.8 0 0 1-8.6-3.1 19.5 19.5 0 0 1-6-6A19.8 19.8 0 0 1 2.1 4.2 2 2 0 0 1 4.1 2h3a2 2 0 0 1 2 1.7c.1.9.4 1.8.7 2.7a2 2 0 0 1-.5 2.1L8 9.8a16 16 0 0 0 6 6l1.3-1.3a2 2 0 0 1 2.1-.4c.9.3 1.8.6 2.7.7a2 2 0 0 1 1.7 2z"/><path d="M15 5a5 5 0 0 1 4 4M15 1a9 9 0 0 1 8 8"/></svg>
        (305) 555-0148 Miami
      </li>
      <li>(954) 555-0172 Broward</li>
      <li>(561) 555-0193 Palm Beach</li>
      <li>
        <svg viewBox="0 0 24 24" fill="none" stroke="#f7b500" stroke-width="2" stroke-linejoin="round"><rect x="2" y="5" width="20" height="14"/><path d="M2 5l10 8 10-8M2 19l7-7M22 19l-7-7"/></svg>
        info@lumvexholdings.com
      </li>
      <li>
        <svg viewBox="0 0 24 24" fill="none" stroke="#6aab08" stroke-width="2"><circle cx="12" cy="12" r="10"/><path d="M2 12h20M12 2a15 15 0 0 1 0 20M12 2a15 15 0 0 0 0 20"/></svg>
        www.lumvexholdings.com
      </li>
    </ul>
  </section>

  <div class="orb orb--orange"></div>
  <div class="orb orb--red"></div>

  <section class="card-back" aria-label="Business card back">
    <div class="project-photo" role="img" aria-label="Photo of technicians working in a warehouse installation, tinted blue"></div>
    <div class="glass"></div>

    <h1 class="headline">
      <span class="headline__top">Low Voltage</span>
      <span class="headline__main">Contractor</span>
    </h1>

    <div class="regions">
      <span class="region region--miami">MIAMI</span>
      <span class="region region--broward">BROWARD</span>
      <span class="region region--palm">PALM BEACH</span>
    </div>

    <div class="brand">
      <span class="brand__dot"></span>
      <p class="brand__name">LUMVEX HOLDINGS</p>
    </div>
  </section>

</body>
</html>
```